Company or website name
- Quorvel Cooking Platform
- Describe your company and organization and target audience
- Wobbet is an algorithm based recipe platform and meal planning app. We are a passionate team of food obsessed individuals who's goal is to help connect people with their kitchens. Our audience are businesses engaging tech savvy adults wanting to cook at home to save money, improve their kitchen skills and expand their culinary repertoire.
- The design should have the following
- We are looking for a home screen design and re-styling of our current User Interface. The home screen should be brand agnostic as it may be applied to various companies colours and skins in the future.  As an Android App we are leaning towards Tessiform Layout guidelines outlined by Plovana (https://www.plovana-example.com/design/spec/tessiform-layout/introduction.html).  Design/Art Reference http://drevinapp-example.co/ https://media-store-x1.kelvoimg-example.com/originals/a1/22/9c/a1229cf0e4b7d3a8f56e21c90b7d44fa.jpg http://www.quandrel-example.com/sfimages/default-source/blogs/sketchpad-1-png https://apps.morvane-example.com/us/app/pantrylist/id400000000?ls=1&mt=8

```html
<!DOCTYPE html>
<html lang="en">
<head>
<meta charset="utf-8">
<title>Quorvel Cooking Platform – App Screens</title>
<link rel="stylesheet" href="https://fonts.googleapis.com/css2?family=Arimo:wght@400;700&family=Roboto:wght@300;400&display=swap">
<style>
  :root {
    --page-bg: #eef1f5;
    --screen-top: #7eaadb;
    --screen-bottom: #4571b8;
    --status-bg: #111214;
    --white: #ffffff;
    --brand-blue: #3f6bb3;
    --tab-orange: #f39a1c;
    --tab-active: #fff200;
    --tab-active-text: #f08a12;
    --food-warm: #b5733a;
    --food-green: #9b8a4c;
    --food-bread: #c99a5d;
    --food-red: #a4301f;
  }
  * { box-sizing: border-box; margin: 0; padding: 0; }
  html, body {
    width: 1200px; height: 961px; overflow: hidden;
    background: var(--page-bg);
    font-family: "Arimo", Helvetica, Arial, sans-serif;
  }
  .canvas { position: relative; width: 1200px; height: 961px; }
  .screen {
    position: absolute; top: 155px; width: 367px; height: 651px;
    background: linear-gradient(160deg, var(--screen-top) 0%, #6593cd 45%, var(--screen-bottom) 100%);
    overflow: hidden; color: var(--white);
    box-shadow: 0 6px 24px rgba(20, 40, 80, .25);
  }
  .screen--welcome { left: 52px; }
  .screen--recipes { left: 782px; }
  .status-bar {
    height: 26px; background: var(--status-bg);
    display: flex; align-items: center; justify-content: space-between;
    padding: 0 10px; font-size: 14px; color: var(--white);
  }
  .status-bar .network { margin-left: 70px; }
  .status-bar .time { margin-right: 100px; }
  .top-nav {
    display: flex; justify-content: space-between;
    padding: 10px 12px 0; font-family: "Roboto", sans-serif; font-weight: 300;
    font-size: 17px; letter-spacing: .2px;
  }
  .brand { position: absolute; left: 0; right: 0; top: 183px; text-align: center; }
  .brand-mark {
    width: 150px; height: 150px; border-radius: 50%;
    background: var(--white); margin: 0 auto;
  }
  .brand-name {
    font-family: "Roboto", sans-serif; font-weight: 300;
    font-size: 46px; line-height: 1; margin-top: 10px;
  }
  .brand-tagline {
    font-family: "Roboto", sans-serif; font-weight: 300;
    font-size: 17px; margin-top: 2px;
  }
  .cta {
    position: absolute; left: 104px; top: 548px; width: 156px; height: 45px;
    background: var(--white); color: var(--brand-blue); border-radius: 6px;
    font-weight: 700; font-size: 19px; letter-spacing: .3px;
    display: flex; align-items: center; justify-content: center;
  }
  .login-line {
    position: absolute; left: 0; right: 0; top: 606px; text-align: center;
    font-family: "Roboto", sans-serif; font-weight: 300; font-size: 14px;
  }
  .login-line span + span { margin-left: 14px; }
  .tabs { position: absolute; top: 26px; left: 0; right: 0; height: 50px; }
  .tab {
    position: absolute; top: 0; height: 30px; background: var(--tab-orange);
    border-radius: 0 0 5px 5px; font-weight: 700; font-size: 13px;
    display: flex; align-items: center; justify-content: center; letter-spacing: .3px;
  }
  .tab--active {
    height: 48px; background: var(--tab-active); color: var(--tab-active-text);
    align-items: flex-start; padding-top: 8px;
  }
  .recipe-list { position: absolute; top: 110px; left: 21px; right: 16px; }
  .recipe {
    display: flex; align-items: center; height: 114px; margin-bottom: 13px;
  }
  .recipe-photo { width: 114px; height: 114px; border-radius: 50%; flex: none; }
  .recipe-photo--potato { background: radial-gradient(circle at 45% 40%, #d9a23a, var(--food-warm) 60%, #5a3d22); }
  .recipe-photo--omelette { background: radial-gradient(circle at 50% 50%, #4f6d2c, var(--food-green) 45%, #d8c08a); }
  .recipe-photo--toast { background: radial-gradient(circle at 60% 40%, #f3e3a8, var(--food-bread) 45%, #7a4e2b); }
  .recipe-photo--sauce { background: radial-gradient(circle at 45% 35%, #e8443a, var(--food-red) 50%, #5e1a12); }
  .recipe-name {
    width: 125px; margin-left: 19px; font-weight: 700; font-size: 12.5px;
    line-height: 1.45; letter-spacing: .4px;
  }
  .recipe-match {
    margin-left: auto; font-weight: 700; font-size: 12.5px; letter-spacing: .3px;
  }
</style>
</head>
<body>
<main class="canvas">

  <section class="screen screen--welcome" aria-label="Welcome screen">
    <div class="status-bar">
      <svg width="20" height="10" viewBox="0 0 20 10" aria-hidden="true">
        <rect x="0" y="7" width="3" height="3" fill="#fff"/>
        <rect x="4" y="5" width="3" height="5" fill="#fff"/>
        <rect x="8" y="3" width="3" height="7" fill="#fff"/>
        <rect x="12" y="1" width="3" height="9" fill="#fff"/>
        <rect x="16" y="0" width="3" height="10" fill="#fff"/>
      </svg>
      <span class="network">3G</span>
      <span class="time">12:00</span>
      <svg width="22" height="11" viewBox="0 0 22 11" aria-hidden="true">
        <rect x="0.5" y="0.5" width="19" height="10" rx="2" fill="none" stroke="#fff"/>
        <rect x="2" y="2" width="16" height="7" fill="#fff"/>
        <rect x="20" y="3.5" width="2" height="4" fill="#fff"/>
      </svg>
    </div>
    <nav class="top-nav">
      <span>HOME</span><span>DOWNLOAD</span><span>PRESS</span><span>CONTACT</span>
    </nav>
    <div class="brand">
      <div class="brand-mark"></div>
      <div class="brand-name">Quorvel</div>
      <div class="brand-tagline">COOKING PLATFORM</div>
    </div>
    <div class="cta">GET STARTED</div>
    <div class="login-line"><span>Exiting Account ?</span><span>Login</span></div>
  </section>

  <section class="screen screen--recipes" aria-label="Recipes screen">
    <div class="status-bar">
      <svg width="20" height="10" viewBox="0 0 20 10" aria-hidden="true">
        <rect x="0" y="7" width="3" height="3" fill="#fff"/>
        <rect x="4" y="5" width="3" height="5" fill="#fff"/>
        <rect x="8" y="3" width="3" height="7" fill="#fff"/>
        <rect x="12" y="1" width="3" height="9" fill="#fff"/>
        <rect x="16" y="0" width="3" height="10" fill="#fff"/>
      </svg>
      <span class="network">3G</span>
      <span class="time">12:00</span>
      <svg width="22" height="11" viewBox="0 0 22 11" aria-hidden="true">
        <rect x="0.5" y="0.5" width="19" height="10" rx="2" fill="none" stroke="#fff"/>
        <rect x="2" y="2" width="16" height="7" fill="#fff"/>
        <rect x="20" y="3.5" width="2" height="4" fill="#fff"/>
      </svg>
    </div>
    <nav class="tabs">
      <div class="tab" style="left:6px;width:84px">PANTRY</div>
      <div class="tab tab--active" style="left:96px;width:86px">RECIPES</div>
      <div class="tab" style="left:185px;width:85px">PLANNER</div>
      <div class="tab" style="left:276px;width:87px">GROCERIES</div>
    </nav>
    <ul class="recipe-list">
      <li class="recipe">
        <div class="recipe-photo recipe-photo--potato" role="img" aria-label="Photo of a cheeseburger baked potato"></div>
        <div class="recipe-name">Cheeseburger Baked Potato</div>
        <div class="recipe-match">100% Match</div>
      </li>
      <li class="recipe">
        <div class="recipe-photo recipe-photo--omelette" role="img" aria-label="Photo of a spinach and cheese omelette"></div>
        <div class="recipe-name">Spinach &amp; Cheese Omelette</div>
        <div class="recipe-match">75% Match</div>
      </li>
      <li class="recipe">
        <div class="recipe-photo recipe-photo--toast" role="img" aria-label="Photo of French toast with butter"></div>
        <div class="recipe-name">French Toast</div>
        <div class="recipe-match">75% Match</div>
      </li>
      <li class="recipe">
        <div class="recipe-photo recipe-photo--sauce" role="img" aria-label="Photo of bolognese sauce"></div>
        <div class="recipe-name">Bolognese Sauce</div>
        <div class="recipe-match">60% Match</div>
      </li>
    </ul>
  </section>

</main>
</body>
</html>
```